Hollarin Painting

Need business card design

Target Market(s)

Paint

Industry/Entity Type

Painting

Requirements
Must have
• Brice Halvorsen | Superviser
| HollaRin Painting
| mobile: (360) 555-0148
| email: Brice@hollarininc.example
| site: www.hollarininc.example
| address: 718 Marbeck St NE Ste 300, Olympia, WA 98577

```html
<!DOCTYPE html>
<html lang="en">
<head>
<meta charset="utf-8">
<title>Hollarin Painting – Business Card</title>
<link rel="stylesheet" href="https://fonts.googleapis.com/css2?family=Arimo:wght@400&family=Tinos:wght@700&display=swap">
<style>
  :root {
    --stage: #2b2b2b;
    --brand-green: #62bf22;
    --brand-blue: #1b3d8c;
    --card-white: #ffffff;
    --ink: #1a1a1a;
    --divider: #8c8c8c;
  }
  * { box-sizing: border-box; margin: 0; padding: 0; }
  html, body { width: 1200px; height: 1015px; overflow: hidden; }
  body {
    background: var(--stage);
    display: flex;
    flex-direction: column;
    align-items: center;
    justify-content: center;
    gap: 58px;
  }
  .card {
    position: relative;
    width: 760px;
    height: 434px;
    overflow: hidden;
    box-shadow: 0 10px 30px rgba(0,0,0,.5);
  }
  .card--front {
    background: var(--brand-green);
    display: flex;
    align-items: center;
    justify-content: center;
  }
  .brand {
    display: flex;
    align-items: center;
    gap: 14px;
    font-family: "Tinos", "Times New Roman", serif;
    font-weight: 700;
    font-size: 46px;
    letter-spacing: 1px;
    text-transform: uppercase;
    line-height: 1;
    white-space: nowrap;
  }
  .brand__mark { width: 22px; height: 22px; flex: none; }
  .card--front .brand { color: var(--card-white); }
  .card--front .brand__mark { background: var(--card-white); }

  .card--back { background: var(--card-white); }
  .card--back .brand {
    position: absolute;
    left: 40px;
    top: 186px;
    width: 340px;
    justify-content: center;
    gap: 10px;
    font-size: 26px;
    letter-spacing: .5px;
    color: var(--brand-blue);
  }
  .card--back .brand__mark { background: var(--brand-green); width: 15px; height: 15px; }
  .divider {
    position: absolute;
    left: 402px;
    top: 70px;
    width: 1px;
    height: 250px;
    background: var(--divider);
  }
  .contact {
    position: absolute;
    left: 430px;
    top: 72px;
    font-family: "Arimo", Arial, sans-serif;
    color: var(--ink);
    font-size: 17px;
    line-height: 1.35;
  }
  .contact__name {
    font-family: "Tinos", "Times New Roman", serif;
    font-weight: 700;
    font-size: 24px;
    color: var(--brand-blue);
    text-transform: uppercase;
    letter-spacing: .5px;
    line-height: 1.1;
  }
  .contact__title { margin-bottom: 12px; }
  .contact__list { list-style: none; }
  .contact__list li { display: flex; align-items: center; gap: 10px; }
  .contact__list svg { width: 17px; height: 17px; flex: none; fill: var(--brand-blue); }
  .contact__address { margin-top: 12px; padding-left: 27px; }
  .band {
    position: absolute;
    bottom: 0;
  }
  .band--green { left: 0; width: 458px; height: 16px; background: var(--brand-green); }
  .band--blue { left: 462px; right: 0; height: 36px; background: var(--brand-blue); }
</style>
</head>
<body>
  <section class="card card--front" aria-label="Card front">
    <div class="brand"><span class="brand__mark"></span>Hollarin Painting</div>
  </section>

  <section class="card card--back" aria-label="Card back">
    <div class="brand"><span class="brand__mark"></span>Hollarin Painting</div>
    <div class="divider"></div>
    <div class="contact">
      <p class="contact__name">Brice Halvorsen</p>
      <p class="contact__title">Superviser</p>
      <ul class="contact__list">
        <li>
          <svg viewBox="0 0 24 24" aria-hidden="true"><path d="M6.6 10.8a15.1 15.1 0 0 0 6.6 6.6l2.2-2.2a1 1 0 0 1 1-.25 11.4 11.4 0 0 0 3.6.57 1 1 0 0 1 1 1V20a1 1 0 0 1-1 1A17 17 0 0 1 3 4a1 1 0 0 1 1-1h3.5a1 1 0 0 1 1 1c0 1.25.2 2.45.57 3.57a1 1 0 0 1-.25 1z"/></svg>
          (360) 555-0148
        </li>
        <li>
          <svg viewBox="0 0 24 24" aria-hidden="true"><path d="M2 5h20v14H2z M2 5l10 8 10-8" stroke="#fff" stroke-width="1.5"/></svg>
          Brice@hollarininc.example
        </li>
        <li>
          <svg viewBox="0 0 24 24" aria-hidden="true"><circle cx="12" cy="12" r="10"/><path d="M2 12h20M12 2c3 3 3 17 0 20M12 2c-3 3-3 17 0 20" stroke="#fff" stroke-width="1.3" fill="none"/></svg>
          www.hollarininc.example
        </li>
      </ul>
      <p class="contact__address">718 Marbeck St NE Ste 300<br>Olympia, WA 98577</p>
    </div>
    <div class="band band--green"></div>
    <div class="band band--blue"></div>
  </section>
</body>
</html>
```